Need a professional card design. Tallowmere building company specialise in residential and commercial builds. New homes, additions & renovations.
Wanting a card with creativity and professionalism.
Want card that utilises logo.

Back and front.

I have just created a logo, and want to use it on the business card.
Attached a copy of the logo.
Attached is also a current business card which I wish to redesign

please utilise both sides

Residential

• Reg# 58306

```html
<!DOCTYPE html>
<html lang="en">
<head>
<meta charset="utf-8">
<title>Tallowmere Building Co — Business Card</title>
<link rel="stylesheet" href="https://fonts.googleapis.com/css2?family=Questrial&family=Montserrat:wght@500;600;700&display=swap">
<style>
  :root {
    --bg: #e9e7e3;
    --card-dark: #2b2624;
    --card-light: #ffffff;
    --gold: #e3a53c;
    --ink: #3a3a3a;
    --ink-soft: #555555;
    --band-dark: #3b3b3b;
  }
  * { box-sizing: border-box; margin: 0; padding: 0; }
  html, body {
    width: 1200px; height: 800px; overflow: hidden;
    background: var(--bg);
    font-family: "Questrial", "Century Gothic", sans-serif;
  }
  .canvas { position: relative; width: 1200px; height: 800px; }

  .card {
    position: absolute; width: 520px; height: 315px;
    box-shadow: 0 6px 18px rgba(0,0,0,0.18);
  }

  /* Back */
  .card-back { left: 70px; top: 110px; background: var(--card-dark); }
  .card-back .brand {
    position: absolute; left: 0; right: 0; top: 100px;
    display: flex; align-items: center; justify-content: center; gap: 10px;
  }
  .brand-dot { width: 12px; height: 12px; border-radius: 50%; background: var(--gold); }
  .brand-name {
    font-family: "Questrial", sans-serif; color: var(--gold);
    font-size: 26px; letter-spacing: 1px;
  }
  .services {
    position: absolute; left: 0; right: 0; top: 200px; text-align: center;
    font-size: 15px; letter-spacing: 0.6px; line-height: 1.4;
  }
  .services .lines { color: #f2f2f2; }
  .services .sectors { color: var(--gold); }

  /* Front */
  .card-front { left: 610px; top: 375px; background: var(--card-light); }
  .card-front .brand {
    position: absolute; left: 40px; top: 62px;
    display: flex; align-items: center; gap: 8px;
  }
  .card-front .brand-name { font-size: 19px; }
  .card-front .brand-dot { width: 10px; height: 10px; }
  .address {
    position: absolute; right: 34px; top: 60px; text-align: right;
    font-size: 11.5px; color: var(--ink); line-height: 1.35;
  }
  .person { position: absolute; left: 40px; top: 205px; }
  .person-name {
    font-family: "Montserrat", sans-serif; font-weight: 700;
    font-size: 13px; color: var(--ink); letter-spacing: 0.4px;
  }
  .person-title { font-size: 11px; color: var(--ink-soft); margin-top: 2px; }
  .contact {
    position: absolute; right: 34px; top: 203px; text-align: right;
    font-size: 11.5px; color: var(--ink); line-height: 1.45;
  }
  .contact .label { font-family: "Montserrat", sans-serif; font-weight: 600; color: var(--gold); }
  .band { position: absolute; left: 0; bottom: 0; width: 520px; height: 22px; display: block; }
</style>
</head>
<body>
<main class="canvas">

  <section class="card card-back" aria-label="Card back">
    <div class="brand">
      <span class="brand-dot"></span>
      <span class="brand-name">Tallowmere Building Co</span>
    </div>
    <div class="services">
      <p class="lines">NEW HOMES - ADDITIONS - RENOVATIONS</p>
      <p class="sectors">DOMESTIC &amp; COMMERCIAL</p>
    </div>
  </section>

  <section class="card card-front" aria-label="Card front">
    <div class="brand">
      <span class="brand-dot"></span>
      <span class="brand-name">Tallowmere Building Co</span>
    </div>
    <address class="address">
      42 Belmont Way<br>
      Ashgrove, WA 6030
    </address>
    <div class="person">
      <p class="person-name">MARA KESWICK</p>
      <p class="person-title">Director</p>
    </div>
    <div class="contact">
      <p><span class="label">Tel:</span> 08 94102267 · <span class="label">Mob:</span> 0412 508 316</p>
      <p><span class="label">Email:</span> tallowmerebuilding@mail.com</p>
    </div>
    <svg class="band" viewBox="0 0 520 22" aria-hidden="true">
      <polygon points="0,8 238,8 226,22 0,22" fill="var(--gold)"/>
      <polygon points="244,0 520,0 520,22 230,22" fill="var(--band-dark)"/>
    </svg>
  </section>

</main>
</body>
</html>
```